Non-Profit org for new mothers in distress in need of website design

We need a website for our non-profit organization, Cradlewell Alliance of Florida, based in Sarasota, Florida. We provide peer support for new moms in distress, trainings for mental health professionals, education and resources for our providers, and an intensive volunteer training program. We need a site that is calming yet energizing, simple, yet informative, with minimal pages and text. Our goal is to be a point of contact for mothers to find local resources whatever their need, so our most important feature we need is at least 4 zip code look-ups for users to find 1. Local volunteers, 2. Support Groups, 3. Trained Mental Health Professionals, 4. Other Health and Wellness Support Providers. Ideally I would like the zip code lookups on the home page sort of interest-layout-style, with the following pages: About Us, PPD Facts, For Parents, For Providers, Donate, Contact, and Blog. Because we are a very small non-profit - under 20 volunteers, no paid staff, donation funded, under $10,000 budget all going to service programs, we can't afford much, but are willing to pay a reasonable fee for quality work. Currently we have an active site through plonto... www.cradlewellhaven.org. The site either needs to be polished or overhauled. And we need a more professional zip code L/U. Thank you so much for your time and interest - we look forward to working with you.
Best,
Maren Tolliver

Reason: Hoping for a couple more changes and clearance with decision-making committee.

Target Market(s)

New mothers with babies and young children, new fathers and perinatal providers

Industry/Entity Type

Non Profit

Number of Pages Required

5+ page

Font styles to use
Sans Serif

Colors
886aae

Requirements
Must have
• contact form, zip code lookup, video embedded, calm and energizing tone
Nice to have
• boardly-style layout
Should not have
• complicated navigation, heavy text,

```html
<!DOCTYPE html>
<html lang="en">
<head>
<meta charset="utf-8">
<title>Cradlewell Alliance of Florida</title>
<link href="https://fonts.googleapis.com/css2?family=Montserrat:wght@300;400;600;700&display=swap" rel="stylesheet">
<style>
:root{
  --brand:#886aae;
  --brand-band:#977dbb;
  --brand-soft:rgba(150,118,205,.74);
  --hero-a:#8f6c9c;
  --hero-b:#c7a6c2;
  --page:#eeedf2;
  --white:#ffffff;
  --footer:#7d7d7d;
  --kinly:#4a6fb5;
  --murmur:#3fa9e6;
  --hearthly:#d9553f;
}
*{box-sizing:border-box;margin:0;padding:0}
html,body{width:1024px;height:1200px;overflow:hidden}
body{background:var(--page);font-family:"Montserrat",sans-serif;color:var(--white);position:relative}
.hero{position:absolute;left:0;top:0;width:1024px;height:304px;
  background:
    radial-gradient(ellipse 260px 160px at 220px 120px,rgba(230,205,225,.55),transparent 70%),
    radial-gradient(ellipse 300px 200px at 820px 160px,rgba(225,195,220,.5),transparent 70%),
    radial-gradient(ellipse 200px 120px at 520px 40px,rgba(120,85,130,.35),transparent 70%),
    linear-gradient(120deg,var(--hero-a),var(--hero-b) 45%,#a98aae 70%,var(--hero-a))}
.nav a{position:absolute;top:34px;font-size:14px;font-weight:600;color:rgba(255,255,255,.88);text-decoration:none;letter-spacing:.2px}
.nav a.active{color:var(--white)}
.nav a.active::after{content:"";position:absolute;left:0;right:0;bottom:-6px;height:2px;background:var(--white)}
.brand-tab{position:absolute;left:450px;top:0;width:124px;height:116px}
.brand-tab svg{position:absolute;inset:0}
.brand-tab span{position:absolute;left:0;right:0;top:40px;text-align:center;color:var(--brand);font-size:14px;font-weight:600}
.title{position:absolute;left:0;right:0;top:138px;text-align:center;font-size:45px;font-weight:300;line-height:56px}
.subtitle{position:absolute;left:0;right:0;top:198px;text-align:center;font-size:19px;font-weight:700}
.grid{position:absolute;left:135px;top:234px;width:752px;height:752px;background:var(--white)}
.tile{position:absolute;overflow:hidden}
.tile .photo{position:absolute;inset:0}
.tile .label{position:absolute;left:0;right:0;bottom:0;height:48px;background:var(--brand-soft);padding:0 13px;display:flex;align-items:center;font-size:19px;font-weight:600;line-height:23px}
.tile .label.tall{height:72px}
.play{position:absolute;left:194px;top:96px}
.quote .photo{background:
  radial-gradient(ellipse 90px 120px at 120px 90px,rgba(200,180,225,.5),transparent 70%),
  linear-gradient(160deg,#b49ad4,#a288c8 60%,#9a80c2)}
.quote p{position:absolute;inset:0;display:flex;align-items:center;justify-content:center;text-align:center;font-size:19px;font-weight:600;line-height:37px}
.finder{position:absolute;left:0;top:1011px;width:1024px;height:149px;background:var(--brand-band)}
.finder h2{position:absolute;left:0;right:0;top:25px;text-align:center;font-size:18px;font-weight:600}
.zip{position:absolute;left:224px;top:67px;width:240px;height:32px;background:var(--white);border:1px solid #ddd;color:#b9b9b9;font-size:15px;padding:0 23px;display:flex;align-items:center;font-weight:300}
.kind{position:absolute;left:464px;top:67px;width:240px;height:32px;background:#f1f1f1;border:1px solid #ddd;color:#888;font-size:15px;display:flex;align-items:center;justify-content:center;gap:8px}
.find{position:absolute;left:705px;top:67px;width:136px;height:32px;background:var(--white);border:1px solid var(--brand);color:var(--brand);font-size:14px;font-weight:700;display:flex;align-items:center;justify-content:center}
.footer{position:absolute;left:0;top:1160px;width:1024px;height:40px;background:var(--footer);font-size:11px;font-weight:400}
.footer p{position:absolute;left:32px;top:13px}
.social{position:absolute;right:32px;top:8px;display:flex;gap:13px}
.social a{width:23px;height:23px;border-radius:50%;display:flex;align-items:center;justify-content:center;color:var(--white);font-size:11px;font-weight:700;text-decoration:none}
.social .kinly{background:var(--kinly)}
.social .murmur{background:var(--murmur)}
.social .hearthly{background:var(--hearthly)}
</style>
</head>
<body>
<header class="hero" role="img" aria-label="Soft purple-toned photo of a mother resting cheek to cheek with her sleeping newborn"></header>
<nav class="nav">
  <a class="active" href="#" style="left:108px">HOME</a>
  <a href="#" style="left:182px">ABOUT</a>
  <a href="#" style="left:264px">PPD</a>
  <a href="#" style="left:322px">FOR MOMS</a>
  <a href="#" style="left:623px">FOR PROVIDERS</a>
  <a href="#" style="left:766px">DONATE</a>
  <a href="#" style="left:855px">BLOG</a>
  <a href="#" style="left:924px">CONTACT</a>
</nav>
<div class="brand-tab">
  <svg width="124" height="116" viewBox="0 0 124 116"><path d="M0 0H124V98L62 116L0 98Z" fill="#fff" stroke="#c9b9de" stroke-width="1"/></svg>
  <span>Cradlewell</span>
</div>
<h1 class="title">Cradlewell Alliance of Florida</h1>
<p class="subtitle">- Cradlewell FL -</p>

<main class="grid">
  <div class="tile" style="left:8px;top:8px;width:438px;height:240px">
    <div class="photo" role="img" aria-label="Video still of a woman in a purple blouse speaking about postpartum support" style="background:
      radial-gradient(ellipse 110px 130px at 250px 90px,rgba(225,180,140,.75),transparent 70%),
      radial-gradient(ellipse 170px 90px at 240px 220px,rgba(110,90,170,.9),transparent 70%),
      radial-gradient(ellipse 80px 140px at 80px 100px,rgba(140,100,55,.7),transparent 70%),
      linear-gradient(110deg,#3f2e1a,#6e5232 40%,#5a4530 70%,#3a2c1c)"></div>
    <svg class="play" width="50" height="50" viewBox="0 0 50 50"><circle cx="25" cy="25" r="25" fill="rgba(130,130,130,.75)"/><path d="M19 15L36 25L19 35Z" fill="#fff"/></svg>
  </div>
  <div class="tile" style="left:455px;top:8px;width:289px;height:240px">
    <div class="photo" role="img" aria-label="Photo of a support group comforting a distressed mother" style="background:
      radial-gradient(ellipse 60px 90px at 150px 110px,rgba(90,130,185,.8),transparent 70%),
      radial-gradient(ellipse 60px 80px at 250px 140px,rgba(200,180,160,.7),transparent 70%),
      radial-gradient(ellipse 50px 80px at 50px 100px,rgba(225,215,205,.9),transparent 70%),
      linear-gradient(160deg,#f2f3f5,#dfe1e6 60%,#c9ccd4)"></div>
    <div class="label">Support Groups</div>
  </div>

  <div class="tile" style="left:8px;top:256px;width:240px;height:240px">
    <div class="photo" role="img" aria-label="Photo of a newborn placed on the mother's chest by a nurse" style="background:
      radial-gradient(ellipse 90px 70px at 130px 110px,rgba(240,215,210,.95),transparent 70%),
      radial-gradient(ellipse 100px 60px at 170px 170px,rgba(205,150,130,.85),transparent 70%),
      linear-gradient(170deg,#3aa7ad,#5cbcbe 35%,#d9b2a6 70%)"></div>
    <div class="label">Training</div>
  </div>
  <div class="tile quote" style="left:256px;top:256px;width:240px;height:240px">
    <div class="photo" role="img" aria-label="Faint purple-tinted photo of a mother behind the quote"></div>
    <p>“You are not alone.<br>You are not to blame.<br>With help and effort,<br>you will be well”</p>
  </div>
  <div class="tile" style="left:504px;top:256px;width:240px;height:240px">
    <div class="photo" role="img" aria-label="Photo of two mothers chatting while holding their babies" style="background:
      radial-gradient(ellipse 60px 80px at 50px 70px,rgba(70,45,35,.85),transparent 70%),
      radial-gradient(ellipse 60px 70px at 190px 60px,rgba(225,195,150,.85),transparent 70%),
      radial-gradient(ellipse 70px 60px at 150px 150px,rgba(215,120,160,.7),transparent 70%),
      linear-gradient(150deg,#f2efec,#e6ddd6 55%,#d8cfe0)"></div>
    <div class="label tall">Specialized<br>Perinatal Wellness</div>
  </div>

  <div class="tile" style="left:8px;top:504px;width:240px;height:240px">
    <div class="photo" role="img" aria-label="Photo of a counselor reaching out to a mother" style="background:
      radial-gradient(ellipse 70px 110px at 50px 110px,rgba(95,75,65,.9),transparent 70%),
      radial-gradient(ellipse 70px 90px at 210px 110px,rgba(30,165,155,.85),transparent 70%),
      linear-gradient(150deg,#d7d6d4,#f0f0f0 50%,#e6e6e6)"></div>
    <div class="label tall">Mental Health<br>Professionals</div>
  </div>
  <div class="tile" style="left:256px;top:504px;width:240px;height:240px">
    <div class="photo" role="img" aria-label="Photo of a mother and baby wearing headphones listening to music" style="background:
      radial-gradient(ellipse 70px 70px at 50px 50px,rgba(110,55,40,.85),transparent 70%),
      radial-gradient(ellipse 60px 60px at 200px 150px,rgba(235,205,190,.95),transparent 70%),
      radial-gradient(ellipse 80px 50px at 90px 120px,rgba(225,190,170,.8),transparent 70%),
      linear-gradient(150deg,#f5f3f2,#ece7e4 60%,#f0ebe9)"></div>
    <div class="label tall">Mother-Infant<br>Recovery Music</div>
  </div>
  <div class="tile" style="left:504px;top:504px;width:240px;height:240px">
    <div class="photo" role="img" aria-label="Photo of a smiling woman in a blue top reading a book" style="background:
      radial-gradient(ellipse 60px 70px at 185px 70px,rgba(70,40,30,.9),transparent 70%),
      radial-gradient(ellipse 90px 80px at 180px 170px,rgba(30,130,190,.9),transparent 70%),
      radial-gradient(ellipse 60px 40px at 60px 170px,rgba(190,220,150,.8),transparent 70%),
      linear-gradient(150deg,#f4f4f4,#ececec 60%,#e3e6ea)"></div>
    <div class="label tall">Resourceful<br>Books</div>
  </div>
</main>

<section class="finder">
  <h2>Enter your ZIP Code and find help near you today</h2>
  <div class="zip">Enter your ZIP code</div>
  <div class="kind">SISTER Mom Volunteer
    <svg width="10" height="9" viewBox="0 0 10 9"><path d="M0 0H10L5 9Z" fill="#777"/></svg>
  </div>
  <div class="find">Find</div>
</section>

<footer class="footer">
  <p>© 2016 Maren Tolliver</p>
  <div class="social" aria-label="Social links">
    <a class="kinly" href="#" aria-label="Kinly">K</a>
    <a class="murmur" href="#" aria-label="Murmur">M</a>
    <a class="hearthly" href="#" aria-label="Hearthly">H</a>
  </div>
</footer>
</body>
</html>
```